Digital Marketing Agency Business Card Design Project

We are a boutique marketing agency that provides premium digital marketing services that invlude
- strategic marketing plans
- Plovex Clickreach advertising
- Search engine optimization
- Digital business analytics
- Digital merketing consulting
Business card must have a premium look that makes c clear statement. We provide digital marketing services for multiple languages.

Business card on the back side should have a slogan. Boutique digital marketing.

We always go the extra mile by every project so that clients gep premium solution and 100% satisfaction.

Please design a business card that is one of a kind..

Thank you.

Psd logo uploaded and brief updated.

Target Market(s)

Companies that need strategic online presence that is reached with boutique digital marketing services in all verticals.

Industry/Entity Type

Marketing

Font styles to use
Sans Serif

Requirements
Must have
• Premium and prestigious look.
Nice to have
• Design unique business card that fits with provided logo.
Logo should include:
Tel., E-mail, web address
Business title: one is CEO, second is COO.
Business address.

Try designing dark and light version, dark with the grey-silver from the logo and light just white background with some abstract curves in blue or green.
Should not have
• No old-style design and font
No need to list our services on the business card.

```html
<!DOCTYPE html>
<html lang="en">
<head>
<meta charset="utf-8">
<title>Veltora Business Card – Front and Back</title>
<link rel="stylesheet" href="https://fonts.googleapis.com/css2?family=Questrial&display=swap">
<style>
  :root {
    --page-bg: #e9e6e2;
    --card-white: #ffffff;
    --card-shade: #e4e4e4;
    --brand-blue: #139fdc;
    --brand-green: #8cc43f;
    --ink-grey: #4a4a4a;
    --mark-grey: #6d6d6d;
    --faint-grey: #d3d6d9;
    --text-white: #ffffff;
  }
  * { box-sizing: border-box; margin: 0; padding: 0; }
  html, body {
    width: 1200px;
    height: 1200px;
    overflow: hidden;
  }
  body {
    background: var(--page-bg);
    font-family: "Questrial", "Century Gothic", sans-serif;
    display: flex;
    flex-direction: column;
    align-items: center;
    justify-content: center;
    gap: 60px;
  }
  .card {
    position: relative;
    width: 900px;
    height: 510px;
    background: radial-gradient(ellipse at 55% 40%, var(--card-white) 45%, var(--card-shade) 100%);
    box-shadow: 0 10px 28px rgba(0, 0, 0, 0.22);
    overflow: hidden;
  }

  /* Front */
  .holder {
    position: absolute;
    top: 36px;
    right: 60px;
    text-align: left;
    line-height: 1.05;
  }
  .holder-name { font-size: 42px; color: var(--ink-grey); }
  .holder-title { font-size: 40px; color: var(--brand-blue); }

  .brand {
    position: absolute;
    left: 90px;
    top: 170px;
    display: flex;
    align-items: center;
    gap: 22px;
  }
  .brand-square {
    width: 30px;
    height: 30px;
    background: var(--brand-green);
  }
  .brand-name {
    font-size: 92px;
    letter-spacing: 4px;
    color: var(--mark-grey);
  }

  .accent-line {
    position: absolute;
    left: 0;
    right: 0;
    top: 312px;
    height: 5px;
    background: var(--brand-green);
  }
  .contact-band {
    position: absolute;
    left: 0;
    right: 0;
    top: 317px;
    bottom: 0;
    background: var(--brand-blue);
    color: var(--text-white);
    font-size: 32px;
  }
  .contact-col {
    position: absolute;
    display: flex;
    flex-direction: column;
    gap: 16px;
  }
  .contact-col--left { left: 60px; bottom: 30px; }
  .contact-col--right { right: 110px; top: 24px; }
  .contact-item {
    display: flex;
    align-items: center;
    gap: 14px;
  }
  .contact-icon { width: 28px; height: 28px; flex: none; }

  /* Back */
  .slogan-band {
    position: absolute;
    left: 0;
    right: 0;
    top: 70px;
    height: 90px;
    background: var(--brand-blue);
    color: var(--text-white);
    font-size: 44px;
    display: flex;
    align-items: center;
    justify-content: flex-end;
    padding-right: 60px;
  }
  .back-brand {
    position: absolute;
    left: 70px;
    top: 240px;
    display: flex;
    align-items: center;
    gap: 20px;
  }
  .back-brand .brand-square { background: var(--faint-grey); width: 40px; height: 40px; }
  .back-brand .brand-name { color: var(--faint-grey); font-size: 120px; }
</style>
</head>
<body>

  <section class="card card--front" aria-label="Business card front">
    <div class="holder">
      <div class="holder-name">Name</div>
      <div class="holder-title">CEO</div>
    </div>

    <div class="brand">
      <span class="brand-square"></span>
      <span class="brand-name">Veltora</span>
    </div>

    <div class="accent-line"></div>

    <div class="contact-band">
      <div class="contact-col contact-col--right">
        <div class="contact-item">
          <svg class="contact-icon" viewBox="0 0 24 24" aria-hidden="true">
            <path fill="#fff" d="M12 2a7 7 0 0 0-7 7c0 5 7 13 7 13s7-8 7-13a7 7 0 0 0-7-7zm0 9.5A2.5 2.5 0 1 1 12 6.5a2.5 2.5 0 0 1 0 5z"/>
          </svg>
          <span>Business Address</span>
        </div>
        <div class="contact-item">
          <svg class="contact-icon" viewBox="0 0 24 24" aria-hidden="true">
            <path fill="#fff" d="M6.6 10.8a15.1 15.1 0 0 0 6.6 6.6l2.2-2.2a1 1 0 0 1 1-.25 11.4 11.4 0 0 0 3.6.57 1 1 0 0 1 1 1V20a1 1 0 0 1-1 1A17 17 0 0 1 3 4a1 1 0 0 1 1-1h3.5a1 1 0 0 1 1 1c0 1.25.2 2.45.57 3.57a1 1 0 0 1-.25 1z"/>
          </svg>
          <span>Phone</span>
        </div>
      </div>

      <div class="contact-col contact-col--left">
        <div class="contact-item">
          <svg class="contact-icon" viewBox="0 0 24 24" aria-hidden="true">
            <rect x="2" y="5" width="20" height="14" fill="#fff"/>
            <path d="M2 5l10 8 10-8" fill="none" stroke="#139fdc" stroke-width="1.8"/>
          </svg>
          <span>Mail</span>
        </div>
        <div class="contact-item">
          <svg class="contact-icon" viewBox="0 0 24 24" aria-hidden="true">
            <g fill="none" stroke="#fff" stroke-width="1.6">
              <circle cx="12" cy="12" r="9.5"/>
              <ellipse cx="12" cy="12" rx="4.2" ry="9.5"/>
              <path d="M2.5 12h19M4 7h16M4 17h16"/>
            </g>
          </svg>
          <span>Web Address</span>
        </div>
      </div>
    </div>
  </section>

  <section class="card card--back" aria-label="Business card back">
    <div class="slogan-band">Boutique Digital Marketing</div>
    <div class="back-brand">
      <span class="brand-square"></span>
      <span class="brand-name">Veltora</span>
    </div>
  </section>

</body>
</html>
```